I need a complete stationary pack for a real estate office that sells and manages residential proper

We need a stationary design pack for my real estate office called ‘wevaultestate’ that is in Queensland Australia. My offices are both in suburban and coastal locations in the south west corner of Queensland at the Sunshine Coast and Brisbane.
We predominately manage real estate on behalf of owners and sell property in the residential sector.
I have attached a copy of our existing design of my business card and do like the current concept/layout. In saying this you may be able to use this existing theme across to the other items required or see opportunity on how to improve what I have already.
I would like to see concepts for the following products:
- Letterhead
- Fax header
- Business cards
- Email signature
- With complements slips and
- Envelopes
I have attached our current logo that was designed by Artflockly and the font is Prelo.

I am looking for a contemporary design that is professional and reflects trust and professionalism. I am currently using the logo with a black background on some material as per the following link

http://www.plotmarket.example.au/listing/for-sale/house/qld/tarrin/?adid=7305184422&sp=3

I have posted another job 517386 for signage and the company car signage done too if you are interested.

Please do not hesitate to contact me should you have any questions. Thank you.

Target Market(s)

Western speaking people aged from 25 to 60 from modest backgrounds to well off individuals

Industry/Entity Type

Real Estate

Requirements
Must have
• Professional in appearance, show a mature and trustworthy image
Should not have
• As there is good colour with the logo, i am do not want over the top designs or colours

```html
<!DOCTYPE html>
<html lang="en">
<head>
<meta charset="utf-8">
<title>wevaultestate – business card</title>
<link rel="stylesheet" href="https://fonts.googleapis.com/css2?family=Open+Sans:wght@400;600;700&display=swap">
<style>
  :root {
    --backdrop: #e9e6e1;
    --card-white: #ffffff;
    --navy-deep: #232c3b;
    --navy-mid: #36435a;
    --ink: #3b4150;
    --grey-text: #5c6068;
    --name-red: #d9363e;
    --title-blue: #3a8fd0;
    --band-blue: #2a9ad8;
    --band-green: #3aa84a;
    --band-purple: #7b3fa0;
    --band-red: #d9303b;
    --icon-green: #4aa54a;
  }
  * { box-sizing: border-box; margin: 0; padding: 0; }
  html, body {
    width: 1200px; height: 1200px; overflow: hidden;
    background: var(--backdrop);
    font-family: "Open Sans", Arial, sans-serif;
  }
  .sheet { position: relative; width: 1200px; height: 1200px; }
  .card {
    position: absolute; left: 150px; width: 900px; height: 514px;
    overflow: hidden;
    box-shadow: 0 6px 18px rgba(0,0,0,0.18);
  }
  /* Back side */
  .card-back {
    top: 60px;
    background: radial-gradient(ellipse at 55% 45%, var(--navy-mid) 0%, var(--navy-deep) 75%);
    display: flex; align-items: center; justify-content: center;
  }
  .brand {
    display: flex; align-items: center; gap: 16px;
    font-weight: 700; letter-spacing: -0.5px;
  }
  .brand-dot { border-radius: 50%; flex: none; }
  .card-back .brand { font-size: 64px; color: #ffffff; }
  .card-back .brand-dot { width: 58px; height: 58px; background: #ffffff; }

  /* Front side */
  .card-front { top: 626px; background: var(--card-white); }
  .card-front .brand {
    position: absolute; left: 86px; top: 112px;
    font-size: 46px; color: var(--ink);
  }
  .card-front .brand-dot { width: 44px; height: 44px; background: var(--ink); }

  .colour-band {
    position: absolute; left: 0; right: 0; bottom: 0; height: 96px;
    background: linear-gradient(90deg,
      var(--band-blue) 0%, var(--band-green) 35%,
      var(--band-purple) 70%, var(--band-red) 100%);
    opacity: 0.85;
  }

  .contact {
    position: absolute; left: 520px; top: 150px;
    color: var(--grey-text);
  }
  .person-name { font-size: 27px; font-weight: 700; color: var(--name-red); line-height: 1.1; }
  .person-role { font-size: 22px; font-weight: 600; color: var(--title-blue); line-height: 1.15; }
  .mobile { font-size: 17px; margin-top: 4px; margin-bottom: 14px; }
  .contact-list { list-style: none; font-size: 17px; line-height: 1.3; }
  .contact-list li { display: flex; align-items: flex-start; gap: 10px; }
  .contact-list svg { width: 18px; height: 18px; flex: none; margin-top: 2px; }
</style>
</head>
<body>
<main class="sheet">

  <section class="card card-back" aria-label="Business card back">
    <div class="brand"><span class="brand-dot"></span><span>wevaultestate</span></div>
  </section>

  <section class="card card-front" aria-label="Business card front">
    <div class="colour-band" role="img" aria-label="Decorative multicolour wave band in blue, green, purple and red"></div>

    <div class="brand"><span class="brand-dot"></span><span>wevaultestate</span></div>

    <div class="contact">
      <p class="person-name">Marcus Tellane</p>
      <p class="person-role">Principal</p>
      <p class="mobile">0428615907</p>
      <ul class="contact-list">
        <li>
          <svg viewBox="0 0 24 24"><path d="M12 2a7 7 0 0 0-7 7c0 5 7 13 7 13s7-8 7-13a7 7 0 0 0-7-7zm0 9.5A2.5 2.5 0 1 1 12 6.5a2.5 2.5 0 0 1 0 5z" fill="var(--icon-green)"/></svg>
          <span>shop 4, 212 harbour way,<br>tarrin qld 4581</span>
        </li>
        <li>
          <svg viewBox="0 0 24 24"><path d="M6.6 10.8a15 15 0 0 0 6.6 6.6l2.2-2.2a1 1 0 0 1 1-.25 11.4 11.4 0 0 0 3.6.57 1 1 0 0 1 1 1V20a1 1 0 0 1-1 1A17 17 0 0 1 3 4a1 1 0 0 1 1-1h3.5a1 1 0 0 1 1 1c0 1.25.2 2.45.57 3.57a1 1 0 0 1-.25 1z" fill="var(--icon-green)"/></svg>
          <span>07 5590 2741</span>
        </li>
        <li>
          <svg viewBox="0 0 24 24"><path d="M3 5h18v14H3z" fill="var(--icon-green)"/><path d="M3 5l9 7 9-7" fill="none" stroke="#ffffff" stroke-width="1.8"/></svg>
          <span>marcus@wevaultestate.com.au</span>
        </li>
        <li>
          <svg viewBox="0 0 24 24"><circle cx="12" cy="12" r="10" fill="var(--icon-green)"/><path d="M2 12h20M12 2c3 3 3 17 0 20M12 2c-3 3-3 17 0 20" fill="none" stroke="#ffffff" stroke-width="1.4"/></svg>
          <span>www.wevaultestate.com.au</span>
        </li>
      </ul>
    </div>
  </section>

</main>
</body>
</html>
```